Business card and Stationary for Brightwell scanning partners
Corvale Roaming Diagnostics
Business card and Stationary for Brightwell scanning partners - Health
Creative Brief
Corporate
Tobias Wrenfield
President, CEO
2847 fern hollow ln Alderbrook Vale, ST 00000
twrenfield2011@example.com
www.corvaleroamingdiagnostics.example or brightwellscanningpartners.example or both
I don't know the web address till I talk to the web guy but one of those two addresses will be my choice depending on the domain availability I also need the second card for the director of the operation Greta Lindqvar 555 010 0183 gretalindqvar@example.com
The logo and one image related to mobile ultrasound
quenbrol quenbrol
I need number 44 back I deleted it by mistake

```html
<!DOCTYPE html>
<html lang="en">
<head>
<meta charset="utf-8">
<title>Brightwell scanning partners – Stationery Set</title>
<link href="https://fonts.googleapis.com/css2?family=Roboto:wght@400;700&display=swap" rel="stylesheet">
<style>
:root{
  --stage:#a8a8a8;
  --paper:#ffffff;
  --navy:#1f3b9a;
  --blue:#2a57b8;
  --teal:#2fa7a0;
  --green:#8cc63f;
  --ink:#3a3a3a;
  --rule:#c9c9c9;
  --tint:#eef2fa;
}
*{box-sizing:border-box;margin:0;padding:0}
html,body{width:1200px;height:454px;overflow:hidden}
body{background:var(--stage);font-family:"Roboto",Arial,sans-serif;color:var(--ink);position:relative}
.piece{position:absolute;background:var(--paper);overflow:hidden;box-shadow:0 1px 3px rgba(0,0,0,.25)}
.wave{position:absolute;left:0;bottom:0;width:100%;display:block}
.brand{position:absolute;display:flex;flex-direction:column;align-items:center;text-align:center;color:var(--navy);font-weight:700;line-height:1.15}
.brand .mark{width:14px;height:14px;background:var(--navy);margin-bottom:4px}
.brand .name{font-size:9px}
.brand.small .mark{width:7px;height:7px;margin-bottom:2px}
.brand.small .name{font-size:5px}
.tiny{position:absolute;font-size:4px;line-height:1.4;color:var(--ink);white-space:nowrap}

/* presentation folder */
.folder-cover{left:12px;top:26px;width:271px;height:274px;background:linear-gradient(90deg,var(--navy) 0%,var(--blue) 30%,var(--teal) 65%,var(--green) 100%)}
.folder-cover .brand{left:20px;top:120px;width:110px;color:#fff}
.folder-cover .brand .mark{background:#fff}
.folder-inside{left:283px;top:26px;width:274px;height:274px}
.pocket{top:300px;height:144px}
.pocket-left{left:12px;width:271px}
.pocket-right{left:283px;width:274px;border-left:1px solid var(--rule)}

/* disc */
.disc{left:756px;top:31px;width:120px;height:120px;border-radius:50%}
.disc::after{content:"";position:absolute;left:50%;top:50%;width:30px;height:30px;margin:-15px 0 0 -15px;border-radius:50%;background:var(--stage);border:4px solid #e6e6e6}

/* invoice */
.invoice-title{position:absolute;right:8px;top:14px;font-size:6px;font-weight:700;color:var(--navy)}
.invoice-table{position:absolute;left:10px;width:58px;top:80px;border-collapse:collapse;font-size:3.5px}
.invoice-table th,.invoice-table td{border:1px solid var(--rule);padding:1px;height:9px;text-align:left}
.invoice-table th{background:var(--tint);color:var(--navy)}

/* envelope */
.envelope-band{position:absolute;right:0;bottom:0;height:50px;width:110px;background:linear-gradient(90deg,rgba(140,198,63,0) 0%,var(--green) 35%,var(--teal) 70%,var(--navy) 100%)}
</style>
</head>
<body>

<svg width="0" height="0" style="position:absolute">
  <defs>
    <symbol id="swoosh" viewBox="0 0 100 30" preserveAspectRatio="none">
      <path d="M0 14 C30 4 60 26 100 8 L100 30 L0 30Z" fill="#8cc63f"/>
      <path d="M0 17 C30 7 60 28 100 11 L100 30 L0 30Z" fill="#2fa7a0"/>
      <path d="M0 20 C30 10 60 30 100 14 L100 30 L0 30Z" fill="#1f3b9a"/>
    </symbol>
  </defs>
</svg>

<!-- presentation folder -->
<section class="piece folder-cover">
  <div class="brand"><span class="mark"></span><span class="name">Brightwell scanning partners</span></div>
</section>
<section class="piece folder-inside">
  <div class="brand" style="left:50px;top:58px;width:130px"><span class="mark"></span><span class="name">Brightwell scanning partners</span></div>
  <svg class="wave" height="60"><use href="#swoosh"/></svg>
</section>
<section class="piece pocket pocket-left">
  <div class="brand small" style="left:80px;top:96px;width:110px"><span class="mark"></span><span class="name">Brightwell scanning partners</span></div>
</section>
<section class="piece pocket pocket-right">
  <div class="brand small" style="left:82px;top:96px;width:110px"><span class="mark"></span><span class="name">Brightwell scanning partners</span></div>
</section>

<!-- small letterhead -->
<section class="piece" style="left:595px;top:19px;width:142px;height:130px">
  <div class="brand small" style="left:8px;top:8px;width:60px"><span class="mark"></span><span class="name">Brightwell scanning partners</span></div>
  <svg class="wave" height="34"><use href="#swoosh"/></svg>
</section>

<!-- disc -->
<section class="piece disc">
  <div class="brand small" style="left:30px;top:14px;width:60px"><span class="mark"></span><span class="name">Brightwell scanning partners</span></div>
  <svg class="wave" height="36"><use href="#swoosh"/></svg>
</section>

<!-- notepad -->
<section class="piece" style="left:885px;top:24px;width:70px;height:72px">
  <div class="brand small" style="left:5px;top:6px;width:60px"><span class="mark"></span><span class="name">Brightwell scanning partners</span></div>
  <svg class="wave" height="18"><use href="#swoosh"/></svg>
</section>

<!-- compliments slip -->
<section class="piece" style="left:974px;top:29px;width:130px;height:48px">
  <div class="brand small" style="left:6px;top:6px;width:60px"><span class="mark"></span><span class="name">Brightwell scanning partners</span></div>
  <svg class="wave" height="14"><use href="#swoosh"/></svg>
</section>

<!-- business cards -->
<section class="piece" style="left:890px;top:101px;width:95px;height:36px">
  <div class="brand small" style="left:2px;top:4px;width:40px"><span class="mark"></span><span class="name">Brightwell scanning partners</span></div>
  <p class="tiny" style="left:44px;top:5px;font-size:3.3px">Tobias Wrenfield<br>President, CEO<br>twrenfield2011@example.com</p>
  <svg class="wave" height="10"><use href="#swoosh"/></svg>
</section>
<section class="piece" style="left:991px;top:101px;width:108px;height:36px;background:linear-gradient(90deg,var(--navy),var(--teal) 60%,var(--green))">
  <p class="tiny" style="left:6px;top:6px;color:#fff;font-size:3.5px">Greta Lindqvar<br>Director of Operations<br>555 010 0183<br>gretalindqvar@example.com</p>
</section>

<!-- full letterhead -->
<section class="piece" style="left:595px;top:163px;width:139px;height:281px">
  <div class="brand small" style="left:40px;top:14px;width:60px"><span class="mark"></span><span class="name">Brightwell scanning partners</span></div>
  <p class="tiny" style="right:6px;bottom:36px;text-align:right">2847 fern hollow ln Alderbrook Vale, ST 00000<br>www.corvaleroamingdiagnostics.example</p>
  <svg class="wave" height="44"><use href="#swoosh"/></svg>
</section>

<!-- invoice form -->
<section class="piece" style="left:749px;top:163px;width:144px;height:281px">
  <div class="brand small" style="left:8px;top:12px;width:60px"><span class="mark"></span><span class="name">Brightwell scanning partners</span></div>
  <p class="invoice-title">Service Invoice</p>
  <p class="tiny" style="left:10px;top:52px">Billed to: Patient account<br>Date of visit:</p>
  <table class="invoice-table">
    <tr><th>Date</th><th>Service</th><th>Qty</th><th>Total</th></tr>
    <tr><td></td><td></td><td></td><td></td></tr>
    <tr><td></td><td></td><td></td><td></td></tr>
    <tr><td></td><td></td><td></td><td></td></tr>
    <tr><td></td><td></td><td></td><td></td></tr>
    <tr><td></td><td></td><td></td><td></td></tr>
  </table>
  <svg class="wave" height="44"><use href="#swoosh"/></svg>
</section>

<!-- landscape sheet -->
<section class="piece" style="left:931px;top:163px;width:185px;height:125px">
  <div class="brand small" style="left:62px;top:10px;width:60px"><span class="mark"></span><span class="name">Brightwell scanning partners</span></div>
  <svg class="wave" height="36"><use href="#swoosh"/></svg>
</section>

<!-- envelope -->
<section class="piece" style="left:931px;top:307px;width:197px;height:113px">
  <div class="brand small" style="left:68px;top:6px;width:60px"><span class="mark"></span><span class="name">Brightwell scanning partners</span></div>
  <p class="tiny" style="left:8px;top:34px">2847 fern hollow ln Alderbrook Vale, ST 00000</p>
  <div class="envelope-band"></div>
</section>

</body>
</html>
```